VORELLE Body Scrub and Lotion Label Design

Need designs for new product line, VORELLE, for a day spa in Houston, TX. We are a Japanese inspired day spa and have been opened for 26 years. We are currently in the process of creating a product line of body scrubs and lotions. The product line represent scents based on the 5 Japanese elements hi (Fire), kaze (Aura), tsuchi (Earth), mizu (Water), and sora (Heaven). The final design should have a cohesive Japanese influence and each label should represent the corresponding element. I will need a 3 inch label for the cap of the jar with name, ingredients, design and size. A 3 inch label for description and instruction on use of product on bottom of jar, a wrap around label for jar with the name of the product & description and size, and a full wrap around label for lotion bottles. Below are the links for each of the containers and jar cap.

Jar - https://www.jarbinstocksupply.com/item/J049A
Jar cap - https://www.jarbinstocksupply.com/item/L252
Bottle - https://www.jarbinstocksupply.com/item/B320A

Description for each element for design inspiration:
火 hi (Fire) - Evoking thoughts of cozying up with a warm cup of chai on a cool autumn night, our 火 hi (Fire) Cleansing Body Scrub embodies the virtue of purity while delivering a decadent experience. Organic Japanese honey crystals, organic Japanese black tea and organic sunflower seed oil, exfoliate and renew parched, rough skin while powerful essential oils increase circulation and flush toxins from the skin. Japanese honey, which contains antibacterial, antiseptic, and antioxidant properties, heals and nourishes while glycolic acid, one of honey’s natural alpha hydroxy acids, exfoliates and smooths the skin. As a humectant, honey also revitalizes and soothes overworked, dehydrated skin. Together these powerful ingredients support the skin’s own cell renewal process, and assist in creating smooth, hydrated skin. Rejuvenate, soften, and restore the natural glow of youthful skin with 火 hi (Fire) Cleansing Body Scrub.

Use: Grab a small amount. Massage gently onto surface of dry skin. Add a small amount of warm water and massage gently again. Rinse with warm water, dry and apply 火 hi (Fire) Body Lotion.

Ingredients: Sucrose (Organic Sugar), Organic Helianthus Annuus (Sunflower) Seed Oil, Organic Honey Crystals (Dried Honey, Cane Juice and Molasses), Organic Camellia Sinensis (Black Tea), Mel (Honey), Citrus Medica Limonum (Lemon) Peel Oil, Citrus Junos (Yuzu) Peel Oil, Eucalyptus Globules Leaf Oil, Eugenia Caryophyllus (Clove) Flower Oil, Cinnamonum Zeylanicum (Cinnamon) Leaf Oil, Rosmarinus Officinalis (Rosemary) Leaf Oil, Tocopherol (Vitamin E).
___________________________

Aura - Rouse your senses and renew your dull skin with Aura Body Scrub. Pure Asian Sea salt and Israeli Dead Sea salt, along with Japanese fruit powders, gently exfoliate to reveal fresher, more vibrant skin. Sweet almond, lavender, and clary sage oils soothe body and mind as lemon peel and oils of rosemary and cajeput heal and improve skin clarity. Aura Cleansing Body Scrub also helps protects skin from environmental damage (including UV rays) with the powerful antioxidant, vitamin E. Prepare to show skin that glows with Aura Cleansing Body Scrub.

Use: Grab a small amount. Massage gently onto surface of dry skin. Add a small amount of warm water and massage gently again. Rinse with warm water, dry and apply Aura Body Lotion.

Ingredients: Sodium Chloride (Asian Sea and Israeli Dead Sea Salt), Prunus Amygdalus Dulcis (Sweet Almond) Oil, Lavandula Angustifolia (Lavender) Buds, Rosmarinus Officinalis (Rosemary) Leaf Oil, Citrus Medica Limonum (Lemon) Peel Powder, Citrus Junos (Yuzu) Peel Oil, Melaleuca Cajeputi (Cajeput) Oil, Lavandula Angustifolia (Lavender) Oil, Luffa Cylindrica (Luffa) Fruit Powder, Salvia Sclarea (Clary) Oil, Baphicacanthus Cusia (Nees) Bremek Powder, Tocopherol (Vitamin E).
____________________________

地 tsuchi (Earth) - Imagine yourself surrounded by the beauty of a Japanese sacred grove as your body is cleansed and restored to its natural glowing state with the garden-inspired 地 tsuchi (Earth) Cleansing Body Scrub. Himalayan Pink Salts are organic compliant and hand-mined from deep within the Himalayan Mountains. Himalayan Pink Salts were crystallized more than 200 million years ago, when ancient sea beds were covered by volcanic lava, protecting the salt from modern-day pollution and lending to the belief that it is the purest salt to be found on earth. These ancient salts, along with dried blue cornflowers, jasmine flowers and lavender buds, exfoliate dry skin and prepare for an earthy delite. Pure essential oils of geranium rose, palmarosa, cedarwood and lavender calm the senses while increasing circulation and flushing impurities from the skin. Regain the luster your skin once had with the 地 tsuchi (Earth) Cleansing Body Scrub.

Use: Grab a small amount. Massage gently onto surface of dry skin. Add a small amount of warm water and massage gently again. Rinse with warm water, dry and apply 地 tsuchi (Earth) Body Lotion.

Ingredients: Sodium Chloride (Himalayan Pink Salt), Oryza Sativa (Rice) Bran Oil, Carthamus Tinctorius (Safflower) Seed Oil, Caprylic/Capric Triglyceride (Fractionated Coconut Oil), Lavandula Angustifolia (Lavender) Oil, Lavandula Angustifolia (Lavender) Buds, Jasminum Odoratissimum (Jasmine) Flowers, Pelargonium Capitatum X Radens (Rose Geranium) Oil, Tocopherol (Vitamin E), Cupressus Funebris (Chinese Cedarwood) Bark Oil, Centaurea Cyanus (Cornflower), Cymbopogon Martinii Var Motia (Palmarosa) Oil.
_________________________

水 mizu (Water) - Restore your skin’s natural radiance and clarity. 水 mizu (Water) Cleansing Body Scrub uses Japanese Sea salts (among the purest salts in the world) and Israeli Dead Sea salt (rich in nourishing minerals) to exfoliate and reveal refreshed skin. Soy seed aids in exfoliation and also provides lecithin and lipids for repairing and regenerating skin cells. As rosemary oil fights bacteria, improves circulation, and reduces the appearance of broken capillaries and varicose veins, protein-rich sweet almond oil nurtures and soothes. 水 mizu (Water) Cleansing Body Scrub also benefits skin with the anti-inflammatory, antiseptic, and uplifting properties of peppermint, spearmint, and thyme. Protect and replenish your skin with 水 mizu (Water) Cleansing Body Scrub.

Use: Grab a small amount. Massage gently onto surface of dry skin. Add a small amount of warm water and massage gently again. Rinse with warm water, dry and apply 水 mizu (Water) Body Lotion.

Ingredients: Sodium Chloride (Mediterranean Sea and Israeli Dead Sea Salt), Prunus Amygdalus Dulcis (Sweet Almond) Oil, Glycine Soja (Soy) Seeds, Rosmarinus Officinalis (Rosemary) Leaf Oil, Mentha Spicata (Spearmint) Leaf Oil, Mentha Piperita (Peppermint) Leaf, Thymus Zygis (Thyme) Oil, Urtica Dioica (Nettle) Leaf Powder, Tocopherol (Vitamin E).
_________________________

空 sora (Heaven) - Refresh and restore balance to your skin with natural exfoliants including organic evaporated cane sugar, luffa fruit powder, and lavender flower, 空 sora (Heaven) Cleansing Body Scrub rejuvenates dull, dry skin. Sweet almond oil, rich in proteins and vitamin D, nourishes and soothes while vitamin C-rich orange peel stimulates circulation and boosts collagen production. As the soft scent of lavender and patchouli oil calms and relaxes the mind, this scrub detoxifies skin, tones, and eases inflammation with orange oil and pink grapefruit oil. With tocopherol (vitamin E), it also helps diminish the signs of aging and protects skin from sun damage and pollutants. Reveal healthier, more balanced skin with our 空 sora (Heaven) Cleansing Body Scrub.

Use: Grab a small amount. Massage gently onto surface of dry skin. Add a small amount of warm water and massage gently again. Rinse with warm water, dry and apply 空 sora (Heaven) Body Lotion.

Ingredients: Organic Sucrose (Sugar), Prunus Amygdalus Dulcis (Sweet Almond) Oil, Citrus Sinensis (Orange) Peel Oil, Citrus Sinensis (Orange) Peel Powder, Luffa Cylindrica Fruit Powder, Lavandula Angustifolia (Lavender) Buds, Carthamus Tinctorius (Safflower) Powder, Citrus Grandis (Pink Grapefruit) Peel Oil, Lavandula Angustifolia (Lavender) Oil, Pogostemon Cablin (Patchouli) Oil, Tocopherol (Vitamin E).

Industry/Entity Type

Skin Care Product

Font styles to use
Other font styles liked:
• Helvetica Neue Slim for the logo VORELLE

Colors

Designer to choose colors to be used in the design.

Requirements
Must have
• My Labels must have the Japanese Kanji symbols for each of the elements characters. Must also have the brand name VORELLE on the label of each product.

```html
<!DOCTYPE html>
<html lang="en">
<head>
<meta charset="utf-8">
<title>Aura Body Scrub &amp; Lotion Labels</title>
<link rel="stylesheet" href="https://fonts.googleapis.com/css2?family=Raleway:wght@300;400;500&display=swap">
<style>
  :root {
    --page: #ffffff;
    --label: #f4f4f3;
    --ink: #1a1a1a;
    --ink-soft: #5a5a5a;
    --ink-faint: #8a8a8a;
    --band: #b9b9b9;
    --edge: #dcdcdc;
  }
  * { margin: 0; padding: 0; box-sizing: border-box; }
  html, body { width: 1200px; height: 887px; overflow: hidden; background: var(--page); }
  body { position: relative; font-family: "Raleway", sans-serif; color: var(--ink); }

  .brand { font-family: "Raleway", sans-serif; font-weight: 300; line-height: 1; color: var(--ink); letter-spacing: 3px; white-space: nowrap; }
  .fine { font-size: 6.2px; line-height: 1.45; color: var(--ink-soft); text-align: justify; }
  .fine b { font-weight: 500; color: var(--ink); }
  .badges { display: flex; gap: 6px; }
  .badge { width: 16px; height: 16px; border-radius: 50%; border: 1.5px solid var(--ink); background: var(--label); }
  .badge.solid { background: var(--ink); }

  /* Jar wrap label */
  .jar-label {
    position: absolute; left: 60px; top: 150px; width: 1080px; height: 130px;
    background: var(--label); border: 1px solid var(--edge);
    display: grid; grid-template-columns: 300px 1fr 300px 40px; align-items: center;
    column-gap: 26px; padding: 0 24px;
  }
  .jar-label .copy { columns: 2; column-gap: 14px; }
  .jar-title { display: flex; align-items: center; justify-content: center; gap: 22px; }
  .jar-title .name { font-size: 20px; font-weight: 400; letter-spacing: .5px; white-space: nowrap; }
  .jar-title .size { font-size: 11px; margin-top: 6px; }
  .jar-title .line { font-size: 20px; font-weight: 300; color: var(--ink-faint); text-align: right; margin-top: 2px; }
  .jar-title .brand { font-size: 24px; }
  .jar-label .ingredients { columns: 2; column-gap: 14px; }
  .jar-label .badges { flex-direction: column; align-items: center; gap: 8px; }

  /* Lotion bottle wrap label */
  .lotion-label {
    position: absolute; left: 230px; top: 400px; width: 740px; height: 250px;
    background: var(--label); border: 1px solid var(--edge);
    display: grid; grid-template-columns: 1fr 1fr;
  }
  .lotion-label::before, .lotion-label::after {
    content: ""; position: absolute; left: 0; right: 0; height: 8px; background: var(--band);
  }
  .lotion-label::before { top: 0; }
  .lotion-label::after { bottom: 0; }
  .lotion-front { display: flex; flex-direction: column; align-items: center; justify-content: center; text-align: center; }
  .lotion-front .line1 { font-size: 20px; font-weight: 300; color: var(--ink-soft); }
  .lotion-front .line2 { font-size: 19px; font-weight: 400; letter-spacing: .5px; margin-top: 2px; }
  .lotion-front .brand { font-size: 30px; margin: 18px 0 12px; }
  .lotion-front .line { font-size: 24px; font-weight: 300; color: var(--ink-faint); }
  .lotion-front .skin { font-size: 7px; color: var(--ink-faint); margin-top: 8px; }
  .lotion-front .size { font-size: 11px; margin-top: 16px; }
  .lotion-back { padding: 22px 30px 20px; border-left: 1px dashed var(--edge); display: flex; flex-direction: column; gap: 7px; }
  .lotion-back .badges { justify-content: center; margin-top: 4px; }
</style>
</head>
<body>

<section class="jar-label" aria-label="Aura body scrub jar wrap label">
  <p class="fine copy">Rouse your senses and renew your dull skin with Aura Body Scrub. Pure Asian Sea salt and Israeli Dead Sea salt, along with Japanese fruit powders, gently exfoliate to reveal fresher, more vibrant skin. Sweet almond, lavender, and clary sage oils soothe body and mind as lemon peel and oils of rosemary and cajeput heal and improve skin clarity. Aura Cleansing Body Scrub also helps protect skin from environmental damage (including UV rays) with the powerful antioxidant, vitamin E. Prepare to show skin that glows. Use: Grab a small amount. Massage gently onto surface of dry skin. Add a small amount of warm water and massage gently again. Rinse with warm water, dry and apply Aura Body Lotion.</p>

  <div class="jar-title">
    <div>
      <p class="name">[BODY SCRUB]</p>
      <p class="size">8 Oz / 236 g</p>
      <p class="line">Aura</p>
    </div>
    <span class="brand">VORELLE</span>
  </div>

  <p class="fine ingredients"><b>Ingredients:</b> Sodium Chloride (Asian Sea and Israeli Dead Sea Salt), Prunus Amygdalus Dulcis (Sweet Almond) Oil, Lavandula Angustifolia (Lavender) Buds, Rosmarinus Officinalis (Rosemary) Leaf Oil, Citrus Medica Limonum (Lemon) Peel Powder, Citrus Junos (Yuzu) Peel Oil, Melaleuca Cajeputi (Cajeput) Oil, Lavandula Angustifolia (Lavender) Oil, Luffa Cylindrica (Luffa) Fruit Powder, Salvia Sclarea (Clary) Oil, Baphicacanthus Cusia (Nees) Bremek Powder, Tocopherol (Vitamin E).</p>

  <div class="badges">
    <span class="badge"></span>
    <span class="badge"></span>
    <span class="badge"></span>
  </div>
</section>

<section class="lotion-label" aria-label="Aura body lotion bottle wrap label">
  <div class="lotion-front">
    <p class="line1">Body</p>
    <p class="line2">LOTION</p>
    <p class="brand">VORELLE</p>
    <p class="line">Aura</p>
    <p class="skin">for all skin types</p>
    <p class="size">8 Oz / 236 g</p>
  </div>
  <div class="lotion-back">
    <p class="fine">Rouse your senses and renew your dull skin with Aura. Pure Asian Sea salt and Israeli Dead Sea salt, along with Japanese fruit powders, gently exfoliate to reveal fresher, more vibrant skin. Sweet almond, lavender, and clary sage oils soothe body and mind as lemon peel and oils of rosemary and cajeput heal and improve skin clarity. Vitamin E helps protect skin from environmental damage. Prepare to show skin that glows with Aura.</p>
    <p class="fine"><i>Use: Grab a small amount. Massage gently onto surface of dry skin. Add a small amount of warm water and massage gently again. Rinse with warm water, dry and apply Aura Body Lotion.</i></p>
    <p class="fine"><b>Ingredients:</b> Sodium Chloride (Asian Sea and Israeli Dead Sea Salt), Prunus Amygdalus Dulcis (Sweet Almond) Oil, Lavandula Angustifolia (Lavender) Buds, Rosmarinus Officinalis (Rosemary) Leaf Oil, Citrus Medica Limonum (Lemon) Peel Powder, Citrus Junos (Yuzu) Peel Oil, Melaleuca Cajeputi (Cajeput) Oil, Luffa Cylindrica (Luffa) Fruit Powder, Salvia Sclarea (Clary) Oil, Tocopherol (Vitamin E).</p>
    <div class="badges">
      <span class="badge"></span>
      <span class="badge solid"></span>
      <span class="badge"></span>
    </div>
  </div>
</section>

</body>
</html>
```